" Assessoria e consultoria de projetos agropecuários com foco em bovinos. DIFERENCIAIS ? Atendimento personalizado; ? Foco em processos; Melhoria continua - metodologia LEAN ? Foco no cliente e na qualidade do serviço; ? Acompanhamento dos resultados gerados pela consultoria; ? Serviço com conhecimento agregado. Atendimento personalizado: A Brota enxerga a necessidade do contato personalizado com o cliente, demonstrando constantemente que a empresa está interessada em ajudá-lo e trazer soluções para seus problemas. ? Foco em processos: Como a maioria das empresas que prestam consultoria na área estão mais voltadas para TÉCNICAS animal, o foco em processos e gestao por processos torna-se um diferencial da Brota. A empresa poderia aproveitar essa vantagem divulgando a importância do gerenciamento eficaz nas fazendas através dos processos agropecuários. ? Foco no cliente e na qualidade do serviço: Através do atendimento personalizado, o consultor da Brota tem a responsabilidade de manter o comprometimento com o cliente e com a qualidade dos serviços entregues. Assim, a empresa cria uma boa relação com os consumidores, fidelizando-os. ? Acompanhamento dos resultados gerados pela consultoria: Além de prestar consultoria, a Empresa auxilia o cliente a implementar as técnicas e soluções, fazendo o acompanhamento de resultados com indicadores. ? Serviço com maior valor agregado: Através da constante busca por conhecimento na área, a qualidade dos projetos entregues será cada vez maior, consequentemente tornando-os mais eficazes e eficientes. "

```html
<!DOCTYPE html>
<html lang="pt-BR">
<head>
<meta charset="utf-8">
<title>Brota – Cartão de visita</title>
<link href="https://fonts.googleapis.com/css2?family=Montserrat:wght@400;500;600;700&display=swap" rel="stylesheet">
<style>
  :root{
    --bg:#e4e6e8;
    --white:#ffffff;
    --navy:#16233a;
    --navy-deep:#0d1626;
    --green:#1f8a3c;
    --green-light:#2fae4f;
    --silver:#b9bfc6;
    --brand-grey:#8a929c;
    --text:#1d2433;
    --muted:#4c5566;
  }
  html,body{margin:0;padding:0;width:1200px;height:1200px;overflow:hidden;background:var(--bg);font-family:"Montserrat",sans-serif;}
  .canvas{position:relative;width:1200px;height:1200px;}
  .card{position:absolute;left:160px;width:880px;height:503px;border-radius:22px;overflow:hidden;box-shadow:0 10px 30px rgba(0,0,0,.18);}
  .card--front{top:70px;background:var(--white);}
  .card--back{top:627px;background:radial-gradient(ellipse at 40% 35%, #1e2e4a 0%, var(--navy) 45%, var(--navy-deep) 100%);}
  .card__shapes{position:absolute;inset:0;width:100%;height:100%;}

  .brand{position:absolute;text-align:center;}
  .brand__mark{display:flex;align-items:center;justify-content:center;gap:14px;}
  .brand__dot{border-radius:50%;background:var(--green);}
  .brand__name{font-weight:600;letter-spacing:.12em;line-height:1;}
  .brand__tagline{font-weight:500;letter-spacing:.2em;text-transform:uppercase;}

  .card--front .brand{top:80px;right:90px;}
  .card--front .brand__dot{width:26px;height:26px;}
  .card--front .brand__name{font-size:64px;color:var(--brand-grey);}
  .card--front .brand__tagline{font-size:12px;color:var(--brand-grey);margin-top:14px;}

  .card--back .brand{top:180px;left:0;right:0;}
  .card--back .brand__dot{width:34px;height:34px;background:var(--green-light);}
  .card--back .brand__name{font-size:92px;color:#d7dbe0;}
  .card--back .brand__tagline{font-size:15px;color:#c5cad1;margin-top:18px;}

  .person{position:absolute;left:52px;top:150px;border-left:7px solid var(--green);padding-left:14px;}
  .person__name{font-size:27px;font-weight:700;color:var(--text);line-height:1.15;}
  .person__role{font-size:21px;font-weight:400;color:var(--text);line-height:1.2;}

  .contacts{position:absolute;left:56px;top:262px;margin:0;padding:0;list-style:none;}
  .contacts li{display:flex;align-items:center;gap:12px;font-size:17px;color:var(--muted);height:30px;}
  .contacts .icon{width:22px;height:22px;flex:none;}
  .contacts .address{line-height:1.05;font-size:17px;height:46px;}
</style>
</head>
<body>
<div class="canvas">

  <section class="card card--front">
    <svg class="card__shapes" viewBox="0 0 880 503" aria-hidden="true">
      <path d="M0 485 L370 485 L450 405 L720 405 L790 335 L880 335" fill="none" stroke="var(--green)" stroke-width="5"/>
      <path d="M390 503 L465 425 L735 425 L805 355 L880 355 L880 503 Z" fill="var(--navy)"/>
    </svg>

    <div class="brand">
      <div class="brand__mark"><span class="brand__dot"></span><span class="brand__name">BROTA</span></div>
      <div class="brand__tagline">Processos agropecuários</div>
    </div>

    <div class="person">
      <div class="person__name">Nome e Sobrenome</div>
      <div class="person__role">Cargo/Função</div>
    </div>

    <ul class="contacts">
      <li>
        <svg class="icon" viewBox="0 0 22 22"><circle cx="11" cy="11" r="11" fill="var(--green)"/><path d="M7.5 6.5 L9.5 6 L10.5 8.5 L9.3 9.5 Q10.3 11.8 12.5 12.7 L13.5 11.5 L16 12.5 L15.5 14.5 Q10 15 7.5 6.5 Z" fill="#fff"/></svg>
        (00) 0000-0000
      </li>
      <li>
        <svg class="icon" viewBox="0 0 22 22"><circle cx="11" cy="11" r="11" fill="var(--green)"/><rect x="6" y="7.5" width="10" height="7" fill="none" stroke="#fff" stroke-width="1.4"/><path d="M6 7.5 L11 11.5 L16 7.5" fill="none" stroke="#fff" stroke-width="1.4"/></svg>
        contato@exemplo.com
      </li>
      <li class="address">
        <svg class="icon" viewBox="0 0 22 22"><circle cx="11" cy="11" r="11" fill="var(--green)"/><path d="M11 5.5 A3.8 3.8 0 0 1 14.8 9.3 Q14.8 11.5 11 16.5 Q7.2 11.5 7.2 9.3 A3.8 3.8 0 0 1 11 5.5 Z" fill="#fff"/><circle cx="11" cy="9.3" r="1.4" fill="var(--green)"/></svg>
        <span>rua exemplo, 000<br>cidade-UF, CEP: 0000-000</span>
      </li>
      <li>
        <svg class="icon" viewBox="0 0 22 22"><circle cx="11" cy="11" r="11" fill="var(--green)"/><circle cx="11" cy="11" r="4" fill="#fff"/></svg>
        perfil.exemplo/empresa
      </li>
    </ul>
  </section>

  <section class="card card--back">
    <svg class="card__shapes" viewBox="0 0 880 503" aria-hidden="true">
      <path d="M600 40 L700 40 L730 70 L880 70" fill="none" stroke="var(--silver)" stroke-width="2"/>
      <path d="M0 470 L520 470 L600 395 L760 395 L810 345 L880 345" fill="none" stroke="var(--silver)" stroke-width="3"/>
      <path d="M545 503 L620 430 L780 430 L830 380 L880 380 L880 503 Z" fill="var(--green)"/>
    </svg>

    <div class="brand">
      <div class="brand__mark"><span class="brand__dot"></span><span class="brand__name">BROTA</span></div>
      <div class="brand__tagline">Processos agropecuários</div>
    </div>
  </section>

</div>
</body>
</html>
```